Brackwell Toner Refills 2-4-1

We need a flyer design for a new printer cartridge refilling shop that has took over the location, assets and customer base of a Plenvale Toner Hub shop. Our offer is Buy One Get One Free on all printer cartridges. We would like to communicate quality, value for money, fast and friendly service from a local inderpendent business. Somewhere on the flyer should show our 100% money back guarantee and free local delivery. We would also like something where we can capture the customers details, esspesially e-mail so we can send further offers. Our colour scheme is magenta, cyan and yellow.
Price conscience retail and business customers who still want quality
Printer

```html
<!DOCTYPE html>
<html lang="en">
<head>
<meta charset="utf-8">
<title>Brackwell Toner Refills 2-4-1 – Buy One Get One Free Flyer</title>
<link rel="stylesheet" href="https://fonts.googleapis.com/css2?family=Anton&family=Arimo&family=Limelight&family=Oswald:wght@300;400&family=Lobster+Two:ital,wght@1,700&family=Kaushan+Script&display=swap">
<style>
  :root {
    --ink: #000000;
    --paper: #ffffff;
    --paper-tint: #f3f3f3;
    --magenta: #ff1cff;
    --cyan: #1ff0ff;
    --yellow: #fff51a;
    --fold: #7a7a7a;
  }
  html, body {
    margin: 0;
    padding: 0;
    width: 851px;
    height: 1200px;
    overflow: hidden;
    background: var(--paper);
  }
  .flyer {
    display: block;
    width: 851px;
    height: 1200px;
  }
  .outer-frame { fill: var(--paper-tint); stroke: var(--ink); stroke-width: 24; }
  .inner-frame { fill: none; stroke: var(--ink); stroke-width: 2.5; }
  .logo-box { fill: var(--paper); stroke: var(--ink); stroke-width: 2; }
  .logo-text { font-family: "Arimo", Arial, sans-serif; font-size: 31px; fill: var(--ink); }
  .star { fill: var(--paper); stroke: var(--ink); stroke-width: 2; }
  .headline { font-family: "Anton", Impact, sans-serif; font-size: 214px; fill: var(--ink); }
  .ribbon { fill: var(--ink); }
  .ribbon-fold { fill: var(--fold); }
  .ribbon-rule { stroke: var(--paper); stroke-width: 2.5; }
  .ribbon-text { font-family: "Limelight", "Poiret One", serif; font-size: 74px; fill: var(--paper); stroke: var(--ink); stroke-width: 1.5; paint-order: stroke; }
  .ribbon-text-shade { font-family: "Limelight", "Poiret One", serif; font-size: 74px; fill: var(--ink); stroke: var(--paper); stroke-width: 2; }
  .free-word { font-family: "Oswald", "Arial Narrow", sans-serif; font-weight: 300; font-size: 330px; }
  .free-fill { fill: var(--magenta); }
  .free-shadow { fill: var(--ink); }
  .asterisk { font-family: "Arimo", Arial, sans-serif; font-size: 22px; fill: var(--ink); }
  .rule { stroke: var(--ink); stroke-width: 2.5; }
  .script-line { font-family: "Lobster Two", cursive; font-style: italic; font-weight: 700; font-size: 40px; fill: var(--ink); }
  .product-line { font-family: "Oswald", "Arial Narrow", sans-serif; font-weight: 400; font-size: 86px; fill: var(--paper); stroke: var(--ink); stroke-width: 2.5; paint-order: stroke; }
  .band-yellow { fill: var(--yellow); }
  .band-cyan { fill: var(--cyan); }
  .band-magenta { fill: var(--magenta); }
  .seal { fill: var(--ink); }
  .seal-ring { fill: none; stroke: var(--paper); stroke-width: 2.5; }
  .seal-text { font-family: "Oswald", "Arial Narrow", sans-serif; font-weight: 400; fill: var(--paper); }
  .band-script { font-family: "Kaushan Script", cursive; fill: var(--ink); }
  .terms { font-family: "Arimo", Arial, sans-serif; font-size: 15px; fill: var(--ink); }
</style>
</head>
<body>
<svg class="flyer" viewBox="0 0 851 1200" xmlns="http://www.w3.org/2000/svg" role="img" aria-label="Brackwell Toner Refills 2-4-1 flyer: Buy one get one free on all printer cartridges">
  <!-- frames -->
  <rect class="outer-frame" x="12" y="12" width="827" height="1176"/>
  <rect class="inner-frame" x="34" y="34" width="783" height="1131"/>

  <!-- logo area -->
  <g class="brand">
    <rect class="logo-box" x="273" y="67" width="290" height="101"/>
    <text class="logo-text" x="418" y="106" text-anchor="middle">COMPANY</text>
    <text class="logo-text" x="418" y="146" text-anchor="middle">LOGO</text>
  </g>

  <!-- stars -->
  <defs>
    <polygon id="star" points="0,-15 4.4,-5.4 14.3,-4.6 6.9,2.2 8.8,12.1 0,7.2 -8.8,12.1 -6.9,2.2 -14.3,-4.6 -4.4,-5.4"/>
  </defs>
  <g class="stars">
    <use class="star" href="#star" x="168" y="122"/>
    <use class="star" href="#star" x="205" y="122"/>
    <use class="star" href="#star" x="242" y="122"/>
    <use class="star" href="#star" x="598" y="122"/>
    <use class="star" href="#star" x="635" y="122"/>
    <use class="star" href="#star" x="672" y="122"/>
  </g>

  <!-- headline -->
  <text class="headline" x="152" y="370" textLength="538" lengthAdjust="spacingAndGlyphs">BUY ONE</text>

  <!-- ribbon -->
  <g class="ribbon-banner">
    <polygon class="ribbon" points="72,430 220,430 220,530 72,530 118,480"/>
    <polygon class="ribbon" points="765,430 620,430 620,530 765,530 718,480"/>
    <polygon class="ribbon-fold" points="178,490 220,490 220,530"/>
    <polygon class="ribbon-fold" points="665,490 620,490 620,530"/>
    <rect class="ribbon" x="178" y="405" width="487" height="85"/>
    <line class="ribbon-rule" x1="190" y1="459" x2="272" y2="459"/>
    <line class="ribbon-rule" x1="553" y1="459" x2="645" y2="459"/>
    <text class="ribbon-text-shade" x="301" y="495" textLength="237" lengthAdjust="spacingAndGlyphs">GET ONE</text>
    <text class="ribbon-text" x="297" y="491" textLength="237" lengthAdjust="spacingAndGlyphs">GET ONE</text>
  </g>

  <!-- FREE -->
  <g class="free">
    <text class="free-word free-shadow" x="158" y="826" textLength="534" lengthAdjust="spacingAndGlyphs">FREE</text>
    <text class="free-word free-fill" x="152" y="820" textLength="534" lengthAdjust="spacingAndGlyphs">FREE</text>
    <text class="asterisk" x="695" y="588">*</text>
  </g>

  <!-- on all -->
  <line class="rule" x1="155" y1="872" x2="340" y2="872"/>
  <line class="rule" x1="505" y1="872" x2="688" y2="872"/>
  <text class="script-line" x="422" y="884" text-anchor="middle">on all</text>

  <!-- product -->
  <text class="product-line" x="155" y="977" textLength="535" lengthAdjust="spacingAndGlyphs">P<tspan font-size="64">RINTER</tspan> C<tspan font-size="64">ARTRIDGES</tspan></text>

  <!-- guarantee band -->
  <g class="guarantee">
    <rect class="band-yellow" x="15" y="1068" width="425" height="44"/>
    <polygon class="band-magenta" points="415,1090 452,1090 440,1116"/>
    <text class="band-script" x="155" y="1098" font-size="23">Money Back Guarantee</text>
    <circle class="seal" cx="82" cy="1082" r="52"/>
    <circle class="seal-ring" cx="82" cy="1082" r="44"/>
    <text class="seal-text" x="82" y="1099" font-size="44" text-anchor="middle" textLength="70" lengthAdjust="spacingAndGlyphs">100%</text>
  </g>

  <!-- delivery band -->
  <g class="delivery">
    <polygon class="band-cyan" points="440,1037 836,1037 836,1085 420,1085 425,1062"/>
    <text class="band-script" x="475" y="1070" font-size="28">Local Delivery</text>
    <circle class="seal" cx="758" cy="1058" r="60"/>
    <circle class="seal-ring" cx="758" cy="1058" r="52"/>
    <text class="seal-text" x="753" y="1080" font-size="54" text-anchor="middle" textLength="68" lengthAdjust="spacingAndGlyphs">FREE</text>
    <text class="seal-text" x="789" y="1046" font-size="16">*</text>
  </g>

  <text class="terms" x="797" y="1148" text-anchor="end">*Terms and conditions apply</text>
</svg>
</body>
</html>
```